KORBALT

The business want a professional looking business card. We have a scetch we will add but want the extra upgrade, and would like more suggestions for variations of our business cards.

```html
<!DOCTYPE html>
<html lang="en">
<head>
<meta charset="utf-8">
<title>KORBALT – Business Card</title>
<link rel="stylesheet" href="https://fonts.googleapis.com/css2?family=Marcellus&family=Montserrat:wght@400;500;600&display=swap">
<style>
  :root {
    --gold-dark: #b08d4e;
    --gold-mid: #c9a865;
    --gold-light: #edcb89;
    --ink-brown: #5b421a;
    --rule-brown: #6b4f22;
    --navy: #121926;
    --pill-text: #e9c98a;
    --page: #f0f0f0;
  }
  * { margin: 0; padding: 0; box-sizing: border-box; }
  html, body { width: 935px; height: 1200px; overflow: hidden; background: var(--page); }
  .canvas {
    width: 935px; height: 1200px;
    display: flex; flex-direction: column; align-items: center; justify-content: center; gap: 64px;
  }
  .card {
    position: relative; width: 720px; height: 433px; overflow: hidden;
    background: linear-gradient(115deg, var(--gold-dark) 0%, var(--gold-mid) 28%, var(--gold-light) 52%, var(--gold-mid) 74%, var(--gold-dark) 100%);
    box-shadow: 8px 10px 12px rgba(0,0,0,0.28);
    color: var(--ink-brown);
  }

  /* Front */
  .front-band {
    position: absolute; left: 0; right: 0; bottom: 0; height: 87px;
    background: var(--navy); border-top: 7px solid var(--rule-brown);
  }
  .front-brand {
    position: absolute; left: 0; right: 0; top: 120px; text-align: center;
  }
  .front-brand .name {
    font-family: "Marcellus", serif; font-size: 86px; line-height: 1; letter-spacing: 1px;
  }
  .front-brand .since {
    font-family: "Montserrat", sans-serif; font-weight: 600; font-size: 19px;
    letter-spacing: 9px; margin-top: 6px;
  }
  .web-pill {
    position: absolute; left: 50%; top: 322px; transform: translateX(-50%);
    width: 312px; height: 52px; border-radius: 26px;
    background: var(--navy); border: 3px solid var(--gold-mid);
    box-shadow: 0 0 0 2px var(--rule-brown);
    display: flex; align-items: center; justify-content: center;
    font-family: "Montserrat", sans-serif; font-size: 22px; color: var(--pill-text);
  }

  /* Back */
  .back-strip {
    position: absolute; left: 0; top: 0; bottom: 0; width: 80px;
    background: var(--navy); border-right: 9px solid var(--rule-brown);
  }
  .icon-pill {
    position: absolute; left: 62px; width: 52px;
    background: var(--navy); border: 3px solid var(--gold-mid); border-radius: 26px;
    box-shadow: 0 0 0 2px var(--rule-brown);
    display: flex; flex-direction: column; align-items: center; justify-content: space-around;
  }
  .icon-pill svg { width: 24px; height: 24px; fill: var(--pill-text); }
  .icon-pill.person { top: 64px; height: 64px; }
  .icon-pill.contact { top: 218px; height: 164px; padding: 10px 0; }

  .identity { position: absolute; left: 128px; top: 66px; }
  .identity .full-name { font-family: "Marcellus", serif; font-size: 35px; line-height: 1.1; }
  .identity .role { font-family: "Montserrat", sans-serif; font-weight: 600; font-size: 21px; margin-top: 4px; }
  .identity .person-name { font-family: "Montserrat", sans-serif; font-weight: 500; font-size: 16px; margin-top: 6px; }

  .contacts {
    position: absolute; left: 128px; top: 238px; list-style: none;
    font-family: "Montserrat", sans-serif; font-size: 22px;
  }
  .contacts li { height: 44px; line-height: 44px; }

  .back-brand { position: absolute; left: 470px; top: 200px; width: 220px; text-align: center; }
  .back-brand .mark-dot { width: 44px; height: 44px; border-radius: 50%; background: var(--ink-brown); margin: 0 auto 14px; }
  .back-brand .name { font-family: "Marcellus", serif; font-size: 38px; line-height: 1; }
  .back-brand .since { font-family: "Montserrat", sans-serif; font-weight: 600; font-size: 10px; letter-spacing: 4px; margin-top: 4px; }
</style>
</head>
<body>
<main class="canvas">
  <section class="card card-front">
    <div class="front-brand">
      <div class="name">KORBALT</div>
      <div class="since">SINCE 2026</div>
    </div>
    <div class="front-band"></div>
    <div class="web-pill">www.korbalt.llc</div>
  </section>

  <section class="card card-back">
    <div class="back-strip"></div>

    <div class="icon-pill person">
      <svg viewBox="0 0 24 24" aria-hidden="true"><circle cx="12" cy="8" r="5"/><path d="M2 22c0-5 4.5-8 10-8s10 3 10 8z"/></svg>
    </div>
    <div class="identity">
      <div class="full-name">KORBALT SOLVIK</div>
      <div class="role">CEO &amp; FOUNDER</div>
      <div class="person-name">Arne Mikal Solvik</div>
    </div>

    <div class="icon-pill contact">
      <svg viewBox="0 0 24 24" aria-hidden="true"><path d="M3 9c0-3 4-5 9-5s9 2 9 5v2h-5V8H8v3H3z"/><path d="M6 12h12l2 9H4z"/></svg>
      <svg viewBox="0 0 24 24" aria-hidden="true"><path d="M2 5h20v2l-10 6L2 7z"/><path d="M2 9l10 6 10-6v10H2z"/></svg>
      <svg viewBox="0 0 24 24" aria-hidden="true" fill="none"><g fill="none" stroke="#e9c98a" stroke-width="1.8"><circle cx="12" cy="12" r="9.5"/><ellipse cx="12" cy="12" rx="4.5" ry="9.5"/><path d="M2.5 12h19M4 7h16M4 17h16"/></g></svg>
    </div>
    <ul class="contacts">
      <li>004791234567</li>
      <li>korbalt.llc@mailbox.com</li>
      <li>www.korbalt.llc</li>
    </ul>

    <div class="back-brand">
      <div class="mark-dot"></div>
      <div class="name">KORBALT</div>
      <div class="since">SINCE 2026</div>
    </div>
  </section>
</main>
</body>
</html>
```